Business Improvement Consultancy needs web design

I need a web design for my company, that offers support to manufacturing and distribution businesses.

We have worked with a range of organisations to help them get more out of their operational processes and supply chains.

With full end to end supply chain knowledge we help them identify waste in their supply chains that often get overlooked.

We support through a number of offerings

Developing an end to end supply chain strategy

Applying Lean to support the strategy

Interim support network to deliver quick wins and rapid cost improvement

Project Management

Interactive training tools for delivering supply chain best practice.

I have the logos done already, so it is more about look and feel, and the colour schemes etc giving a professional feel.

Also have the web domains www.veltrosiga.co, www.veltrosiga.co.uk & www.veltrosiga.eu, using Q&Q starter bundle

Target Market(s)

Manufacturing and distribution businesses, potentially other consultancies looking for collaboration

Industry/Entity Type

Business

Requirements
Must have
• Some pictures on related to performance improvement, bar charts showing productivity growth / increase.

Should have the chatterbox quipper and worknodes logos to share the website

```html
<!DOCTYPE html>
<html lang="en">
<head>
<meta charset="utf-8">
<title>Veltrosiga Europe</title>
<link href="https://fonts.googleapis.com/css2?family=Open+Sans:wght@300;400;600;700&display=swap" rel="stylesheet">
<style>
:root{
  --navy:#27235f;
  --navy-deep:#1f1a55;
  --navy-light:#4e4c98;
  --tab:#45428f;
  --tab-text:#c9c8ee;
  --link:#c6c5e6;
  --page:#f3f3f3;
  --white:#ffffff;
  --banner:#e8e8e8;
  --rule:#4a4795;
  --body:#3a3a3a;
  --muted:#9a9a9a;
  --quote:#f2f2f2;
  --check:#cfcfcf;
  --placeholder:#dedcd6;
}
*{margin:0;padding:0;box-sizing:border-box}
html,body{width:1200px;height:831px;overflow:hidden;background:var(--page)}
.stage{position:relative;width:1300px;height:900px;transform:scale(0.923077);transform-origin:0 0;font-family:Arial,Helvetica,sans-serif;color:var(--body)}
.masthead{position:absolute;left:0;top:0;width:1300px;height:309px;
  background:radial-gradient(ellipse 260px 360px at 300px 120px,var(--navy-light),rgba(78,76,152,0) 100%),linear-gradient(90deg,#2c2868 0%,var(--navy) 60%,#241f5a 100%);
  border-top:4px solid var(--navy-deep)}
.brand{position:absolute;left:234px;top:54px;display:flex;align-items:center;gap:12px;color:var(--white);font-family:"Open Sans",sans-serif;font-weight:400;font-size:22px}
.brand-dot{width:28px;height:28px;border-radius:50%;background:var(--white)}
.utility{position:absolute;top:23px;left:952px;display:flex;font-size:12px;font-weight:bold}
.utility a{color:var(--link);text-decoration:underline}
.utility .sep{width:1px;height:16px;background:#5a57a0;margin:0 14px}
.nav{position:absolute;top:106px;left:752px;display:flex;gap:2px}
.nav a{height:30px;line-height:30px;text-align:center;font-size:12px;font-weight:bold;text-decoration:none;background:var(--tab);color:var(--tab-text)}
.nav a.active{background:var(--white);color:var(--navy)}
.sheet{position:absolute;left:225px;top:136px;width:900px;height:705px;background:var(--white);box-shadow:0 4px 10px rgba(0,0,0,.05)}
.hero{position:absolute;left:9px;top:10px;width:880px;height:307px;background:var(--banner);overflow:hidden}
.hero-figure{position:absolute;left:11px;top:8px;width:140px;height:299px;background:#dadada}
.hero-chart{position:absolute;left:306px;top:15px;width:552px;height:292px;background:linear-gradient(180deg,#e4e2dc,var(--placeholder))}
.hero-title{position:absolute;left:157px;top:27px;font-family:"Open Sans",sans-serif;font-weight:300;color:var(--navy);font-size:42px;letter-spacing:-1.5px;line-height:50px;white-space:nowrap}
.hero-title b{font-weight:700}
.hero-lede{position:absolute;left:160px;top:81px;font-family:"Open Sans",sans-serif;color:var(--navy);font-size:17.5px;line-height:27px;letter-spacing:-.3px;white-space:nowrap}
.col{position:absolute;top:340px}
.col-head{display:flex;align-items:center;gap:14px;font-family:"Open Sans",sans-serif;font-weight:600;font-size:17px;color:#111;padding:0 0 6px 2px;border-bottom:3px solid var(--rule)}
.col-head .arr{font-size:14px;font-weight:400}
.about{left:13px;width:264px}
.about p{margin-top:14px;font-size:13.5px;line-height:19.3px;width:272px}
.help{left:320px;width:263px}
.help ul{list-style:none;margin-top:21px}
.help li{display:flex;gap:13px;font-size:13px;line-height:16px;margin-bottom:15px}
.tick{flex:none;width:16px;height:16px;background:var(--check);margin-top:1px}
.voices{left:616px;width:270px}
.quote{position:relative;margin:12px 0 0 2px;width:267px;padding:12px;background:var(--quote);font-size:12.5px;line-height:20px}
.quote::after{content:"";position:absolute;right:46px;bottom:-15px;border-top:15px solid var(--quote);border-right:20px solid transparent}
.quote-by{margin:6px 0 0 102px;font-size:11px;color:#222}
.shade{position:absolute;left:10px;top:552px;width:880px;height:6px;background:radial-gradient(ellipse at center top,rgba(0,0,0,.06),rgba(0,0,0,0) 70%)}
.news{position:absolute;left:17px;top:578px;width:570px}
.mini-head{display:flex;gap:12px;font-family:"Open Sans",sans-serif;font-weight:600;font-size:13px;color:#111}
.news p{margin-top:15px;font-size:12.5px;line-height:20px}
.divider{position:absolute;left:622px;top:574px;width:1px;height:90px;background:#e4e4e4}
.connect{position:absolute;left:664px;top:584px}
.social{display:flex;gap:14px;margin-top:18px;margin-left:-2px}
.social a{display:flex;flex-direction:column;align-items:center;gap:3px;text-decoration:none;font-size:9px;color:#666;width:32px;white-space:nowrap}
.social span.c{width:32px;height:32px;border-radius:50%}
.c1{background:#4fb5e3}.c2{background:#4a5a9c}.c3{background:#d8d8d8}.c4{background:#ef8a1f}
.footer{position:absolute;top:856px;left:0;width:1300px;text-align:center;font-family:"Open Sans",sans-serif;font-size:11px;color:var(--muted)}
</style>
</head>
<body>
<div class="stage">
  <header class="masthead">
    <div class="brand"><span class="brand-dot"></span>Veltrosiga Europe</div>
    <nav class="utility"><a href="#">Contact us</a><span class="sep"></span><a href="#">Projects</a></nav>
    <nav class="nav">
      <a class="active" href="#" style="width:88px">HOME</a>
      <a href="#" style="width:120px">SUPPLY CHAIN</a>
      <a href="#" style="width:77px">LEAN</a>
      <a href="#" style="width:82px">INTERIM</a>
    </nav>
  </header>

  <main class="sheet">
    <section class="hero">
      <div class="hero-figure" role="img" aria-label="Faint silhouette of a businessman"></div>
      <div class="hero-chart" role="img" aria-label="Rising 3D bar arrows showing productivity growth"></div>
      <h1 class="hero-title">PRODUCTIVE <b>GROWTH</b></h1>
      <p class="hero-lede">We have worked with a range of organisations to help<br>them get more out of their opertional<br>processes and supply chains.</p>
    </section>

    <section class="col about">
      <h2 class="col-head"><span class="arr">→</span>ABOUT US</h2>
      <p>Welcome to Veltrosiga Europe. With full end to end supply chain knowledge we can help you identify waste in your supply chains that often get overlooked.Before you look to embark on cost reduction plans or a lean journey, get in touch to ensure that your chosen path delivers sustainability and profitable growth.</p>
    </section>

    <section class="col help">
      <h2 class="col-head"><span class="arr">→</span>HOW CAN WE HELP</h2>
      <ul>
        <li><span class="tick"><svg width="16" height="16" viewBox="0 0 16 16"><path d="M4 8.5l2.5 2.5L12 5" fill="none" stroke="#444" stroke-width="1.4"/></svg></span>Developing an end to end supply chain strategy</li>
        <li><span class="tick"><svg width="16" height="16" viewBox="0 0 16 16"><path d="M4 8.5l2.5 2.5L12 5" fill="none" stroke="#444" stroke-width="1.4"/></svg></span>Applying Lean to support the strategy</li>
        <li><span class="tick"><svg width="16" height="16" viewBox="0 0 16 16"><path d="M4 8.5l2.5 2.5L12 5" fill="none" stroke="#444" stroke-width="1.4"/></svg></span>Interim support network to deliver quick wins and repid cost improvement</li>
        <li><span class="tick"><svg width="16" height="16" viewBox="0 0 16 16"><path d="M4 8.5l2.5 2.5L12 5" fill="none" stroke="#444" stroke-width="1.4"/></svg></span>Project Management</li>
      </ul>
    </section>

    <section class="col voices">
      <h2 class="col-head"><span class="arr">→</span>TESTIMONIALS</h2>
      <blockquote class="quote">Lorem ipsum dolor sit amet, consectetur adipiscing elit. Pellentesque quis nulla id orci malesuada porta posuere quis massa. Nunc vitae purus non augue scelerisque ultricies vitae et velit.</blockquote>
      <p class="quote-by">Lorem ipsum dolor</p>
    </section>

    <div class="shade"></div>

    <section class="news">
      <h3 class="mini-head"><span>→</span>LATEST NEWS</h3>
      <p>Lorem ipsum dolor sit amet, consectetur adipiscing elit. Pellentesque quis nulla id orci malesuada porta posuere quis massa. Nunc vitae purus non augue scelerisque ultricies vitae et velit.</p>
    </section>
    <div class="divider"></div>
    <section class="connect">
      <h3 class="mini-head"><span>→</span>CONENCT WITH US</h3>
      <div class="social">
        <a href="#"><span class="c c1"></span>quipper</a>
        <a href="#"><span class="c c2"></span>chatterbox</a>
        <a href="#"><span class="c c3"></span>worknodes</a>
        <a href="#"><span class="c c4"></span>feed</a>
      </div>
    </section>
  </main>

  <footer class="footer">© 2011 Veltrosiga Europe. All Rights Reserved</footer>
</div>
</body>
</html>
```